Redesign of existing site - Brenkow GmbH

Redesign of the following site.
https://www.brenkow-gmbh.example/

The colors red and green need to remain.
Topic: calendar binder

The font "FF Market Regular" should be used s well. But -- if you find a font which is similar and a bit more modern, then go with it. (see font-example.jpg)

The mainpage should have a slider with a video first. Enclosed is a screenshot of the video. (see video.jpg)

Logo also enclosed as svg. The red color might not be quit right. Please check it on your own.
For the second page this page should be used to redesign:
https://www.brenkow-gmbh.example/bindungen/ring-wire-bindung/

I am planing to use the KORVA builder. If you built this in KORVA builder and be able to send me the template or installation (Mirrorkit) that would be a huge advantage.
Updates

IMPORTANT:
I have received many designs in English. But I can't present them to the customer. Please convert them into German, otherwise they cannot be used.

Number of Pages Required

2 page

Requirements
Must have
• Please translate designs into german if it is to be considered. How should I explain a design in english to the customer?

```html
<!DOCTYPE html>
<html lang="de">
<head>
<meta charset="utf-8">
<title>Brenkow Kalenderbindungen</title>
<link href="https://fonts.googleapis.com/css2?family=Dancing+Script:wght@500;600&family=Inter:wght@400;500;600;700;800&display=swap" rel="stylesheet">
<style>
:root{
  --red:#ee0000;
  --red-soft:#e84a4a;
  --ink:#1d1d1d;
  --text:#3a3a3a;
  --muted:#6b6b6b;
  --light:#f5f5f5;
  --line:#e2e2e2;
  --dark:#262626;
  --white:#ffffff;
  --script:"Dancing Script",cursive;
  --sans:"Inter",sans-serif;
}
*{box-sizing:border-box;margin:0;padding:0}
html,body{width:1200px;height:4383px;overflow:hidden}
body{font-family:var(--sans);color:var(--text);background:var(--white);position:relative}
a{color:inherit;text-decoration:none}
.abs{position:absolute}
.script{font-family:var(--script);font-weight:600;color:var(--ink)}
.btn{position:absolute;display:flex;align-items:center;justify-content:center;background:var(--red);color:var(--white);font-size:11px;font-weight:600;border-radius:16px}
.btn-outline{background:var(--white);color:var(--red);border:1.5px solid var(--red)}
.eyebrow{position:absolute;font-size:10px;font-weight:600;color:var(--red)}

/* Header */
.header{position:absolute;left:0;top:0;width:1200px;height:87px;background:var(--white)}
.topbar{position:absolute;right:0;top:0;width:425px;height:24px;background:var(--dark);display:flex;align-items:center;font-size:10px;color:var(--white);clip-path:polygon(22px 0,100% 0,100% 100%,0 100%)}
.topbar .phone{position:absolute;left:0;top:0;height:24px;width:200px;background:var(--white);color:var(--ink);display:flex;align-items:center;justify-content:center;gap:6px;font-weight:600}
.topbar .mail{position:absolute;left:240px;display:flex;align-items:center;gap:6px}
.logo{position:absolute;left:105px;top:22px;font-size:40px;font-weight:800;color:var(--red);letter-spacing:-2px;text-transform:uppercase;line-height:1}
.nav{position:absolute;left:464px;top:48px;display:flex;font-size:11px;font-weight:500;color:var(--ink)}
.nav a{position:absolute;white-space:nowrap}
.nav a.active{color:var(--red)}
.nav a.active::after{content:"";position:absolute;left:0;right:0;top:25px;height:2px;background:var(--red)}

/* Hero */
.hero{position:absolute;left:0;top:87px;width:1200px;height:407px;background:linear-gradient(180deg,#3d3b3a 0%,#5a5754 45%,#3a3837 100%)}
.hero .play{position:absolute;left:573px;top:105px;width:52px;height:52px;border-radius:50%;background:var(--red)}
.hero h1{position:absolute;left:0;width:1200px;top:170px;text-align:center;font-family:var(--script);font-weight:500;font-size:56px;color:var(--white)}

/* About */
.about{position:absolute;left:0;top:494px;width:1200px;height:723px;background:var(--light)}
.about .photo{position:absolute;left:199px;top:74px;width:358px;height:358px;border-radius:8px 8px 70px 8px;background:linear-gradient(135deg,#6f7a86 0%,#a9b2bb 45%,#2f3b5a 75%,#8a9099 100%)}
.about h2{position:absolute;left:613px;top:128px;font-size:37px;line-height:44px;width:420px}
.about p{position:absolute;left:613px;top:272px;width:380px;font-size:10.5px;line-height:19px;color:var(--text)}
.stats-line{position:absolute;left:199px;top:555px;width:800px;height:1px;background:var(--red-soft)}
.stat{position:absolute;top:463px;width:184px;height:184px;border-radius:50%;border:1px solid var(--red-soft);background:radial-gradient(circle at 50% 40%,#fafafa,#ececec);text-align:center}
.stat .k{position:absolute;left:0;right:0;top:50px;font-family:var(--script);font-weight:600;font-size:19px;color:var(--red)}
.stat .v{position:absolute;left:0;right:0;top:78px;font-size:31px;font-weight:500;color:var(--ink)}
.stat .s{position:absolute;left:0;right:0;top:120px;font-family:var(--script);font-size:12px;color:var(--red)}

/* Bindings */
.bindings{position:absolute;left:0;top:1217px;width:1200px;height:550px;background:#f1f1f1}
.section-title{position:absolute;left:0;width:1200px;text-align:center;font-size:38px}
.bindings .sub{position:absolute;left:0;width:1200px;top:130px;text-align:center;font-size:10.5px;font-weight:600;color:var(--ink)}
.bcard{position:absolute;top:175px;width:228px;height:236px;border-bottom:1.5px solid var(--red-soft)}
.bcard .img{height:188px}
.bcard .lbl{height:48px;display:flex;align-items:center;justify-content:center;font-family:var(--script);font-weight:500;font-size:19px;color:var(--ink)}
.bcard.active .lbl{background:var(--red);color:var(--white)}

/* Service */
.service{position:absolute;left:0;top:1767px;width:1200px;height:446px;background:var(--white)}
.scard{position:absolute;top:154px;width:481px;height:219px;border:1px solid var(--red-soft);background:var(--white)}
.scard .img{position:absolute;left:0;top:0;width:194px;height:217px}
.scard .icon{position:absolute;left:157px;top:67px;width:74px;height:74px;border-radius:50%;background:var(--white);display:flex;align-items:center;justify-content:center}
.scard h3{position:absolute;left:243px;top:36px;font-size:23px}
.scard p{position:absolute;left:243px;top:78px;width:215px;font-size:10.5px;line-height:19px}
.scard .btn{left:243px;top:150px;width:121px;height:30px}

/* Team */
.team{position:absolute;left:0;top:2213px;width:1200px;height:715px;background:linear-gradient(180deg,var(--red) 0,var(--red) 463px,#f7f7f7 463px)}
.team .eyebrow{left:0;width:1200px;text-align:center;top:79px;color:var(--white)}
.team h2{position:absolute;left:215px;width:770px;top:103px;text-align:center;font-family:var(--script);font-weight:500;font-size:38px;line-height:44px;color:var(--white)}
.tcard{position:absolute;top:296px;width:481px;height:321px;background:var(--white);border:1px solid #cfcfcf}
.tcard .photo{position:absolute;right:0;top:0;width:264px;height:319px;background:linear-gradient(160deg,#f0f0f0,#d9dadc 60%,#2c3442 61%,#222a36)}
.tcard h3{position:absolute;left:30px;top:60px;font-size:23px;z-index:1}
.tcard .role{position:absolute;left:30px;top:104px;font-size:11px;color:var(--ink)}
.tcard .row{position:absolute;left:30px;display:flex;align-items:center;gap:6px;font-size:10.5px;color:var(--ink)}
.tcard .more{position:absolute;left:30px;top:264px;font-size:10.5px;font-weight:600;color:var(--red);text-decoration:underline}
.arrow{position:absolute;width:30px;height:30px;border-radius:50%;background:var(--white);border:1px solid var(--red-soft);display:flex;align-items:center;justify-content:center}

/* Why */
.why{position:absolute;left:0;top:2928px;width:1200px;height:472px;background:#f7f7f7}
.why h2{position:absolute;left:199px;top:72px;font-size:40px;line-height:44px;width:330px}
.why .tag{position:absolute;left:199px;top:175px;font-family:var(--script);font-weight:600;font-size:25px;color:var(--red)}
.check{position:absolute;display:flex;align-items:center;gap:10px;font-size:12.5px;font-weight:500;color:var(--ink)}
.why .circle{position:absolute;left:739px;top:32px;width:352px;height:352px;border-radius:50%;background:radial-gradient(circle at 45% 45%,#fbfaf6,#ebe7dd 60%,#d8d3c8)}
.why .ring{position:absolute;left:719px;top:32px;width:370px;height:370px;border-radius:50%;border:1.5px solid var(--red-soft)}

/* Gallery */
.gallery{position:absolute;left:0;top:3400px;width:1200px;height:637px;background:var(--light)}
.filters{position:absolute;top:179px;left:354px;height:22px}
.filters span{position:absolute;top:0;height:22px;border:1px solid #cfcfcf;border-radius:11px;background:var(--white);font-size:9px;color:var(--ink);display:flex;align-items:center;justify-content:center;white-space:nowrap}
.filters span.on{background:var(--dark);color:var(--white);border-color:var(--dark)}
.gimg{position:absolute}

/* Footer */
.footer{position:absolute;left:0;top:4037px;width:1200px;height:346px;background:linear-gradient(180deg,#2c2c2c,#1e1e1e);color:#d8d8d8}
.footer .logo{left:199px;top:82px;font-size:40px}
.footer .about-txt{position:absolute;left:199px;top:147px;width:230px;font-size:10.5px;line-height:16px}
.social{position:absolute;top:228px;width:22px;height:22px;border-radius:50%;border:1px solid var(--red)}
.footer h4{position:absolute;top:78px;font-family:var(--script);font-weight:600;font-size:20px;color:var(--white)}
.frow{position:absolute;left:505px;display:flex;align-items:center;gap:8px;font-size:10.5px}
.links a{position:absolute;font-size:10px}
.footer .rule{position:absolute;left:199px;top:288px;width:900px;height:1px;background:#444}
.footer .copy{position:absolute;left:0;width:1200px;top:312px;text-align:center;font-size:10px}
.footer .copy b{color:var(--red);font-weight:400}
</style>
</head>
<body>

<header class="header">
  <div class="topbar">
    <span class="phone"><svg width="11" height="11" viewBox="0 0 24 24"><path fill="#ee0000" d="M6.6 10.8a15 15 0 006.6 6.6l2.2-2.2c.3-.3.7-.4 1-.2 1.1.4 2.3.6 3.6.6.6 0 1 .4 1 1V20c0 .6-.4 1-1 1A17 17 0 013 4c0-.6.4-1 1-1h3.5c.6 0 1 .4 1 1 0 1.3.2 2.5.6 3.6.1.3 0 .7-.2 1z"/></svg>+49 (8421) 5530-0</span>
    <span class="mail"><svg width="11" height="9" viewBox="0 0 24 18"><path fill="#fff" d="M0 0h24v18H0z M2 2l10 7 10-7" stroke="#262626" stroke-width="2"/></svg>info@brenkow-gmbh.example</span>
  </div>
  <a class="logo" href="#">Brenkow</a>
  <nav class="nav">
    <a class="active" style="left:0">Home</a>
    <a style="left:67px">Unternehmen</a>
    <a style="left:178px">Bindungen</a>
    <a style="left:274px">Exklusives</a>
    <a style="left:368px">Galerie</a>
    <a style="left:445px">Service</a>
  </nav>
  <a class="btn" href="#" style="left:980px;top:41px;width:113px;height:31px">Kontakt</a>
</header>

<section class="hero" role="img" aria-label="Standbild aus dem Video: Bindemaschinen in der Produktionshalle">
  <div class="play"><svg width="52" height="52" viewBox="0 0 52 52"><path d="M21 17l14 9-14 9z" fill="#fff"/></svg></div>
  <h1>Brenkow Kalenderbindungen</h1>
  <a class="btn" href="#" style="left:544px;top:269px;width:111px;height:30px">Kontakt</a>
</section>

<section class="about">
  <div class="photo" role="img" aria-label="Foto: Bindemaschine mit Kalenderblättern"></div>
  <span class="eyebrow" style="left:613px;top:96px">Über uns</span>
  <h2 class="script">Ringdrahtbindungen, spiralbindungen und vieles mehr</h2>
  <p>Die industrielle Buchbinderei Brenkow GmbH + Co. KG bietet Ihnen in ihren Kernkompetenzen „Welt der Bindungen“ individuelle und ganzheitliche Lösungen für unterschiedliche Ansprüche. Mit großer Erfahrung und Ideenreichtum beraten wir Sie gerne. Unser Leistungsspektrum reicht von der Planung über die Produktion.</p>
  <a class="btn" href="#" style="left:613px;top:382px;width:119px;height:30px">Mehr Info</a>
  <div class="stats-line"></div>
  <div class="stat" style="left:339px"><span class="k">Brenkow</span><span class="v">56</span><span class="s">Jahre Erfahrung</span></div>
  <div class="stat" style="left:507px"><span class="k">Zufriedene</span><span class="v">+1547</span><span class="s">Kunden</span></div>
  <div class="stat" style="left:676px"><span class="k">Mehr als</span><span class="v">65 Mill.+</span><span class="s">Bindungen</span></div>
</section>

<section class="bindings">
  <h2 class="section-title script" style="top:74px">Die leichtigkeit des blätterns!</h2>
  <p class="sub">Unsere Kalenderbindungen und Bindungen im Überblick.</p>
  <div class="bcard" style="left:106px"><div class="img" role="img" aria-label="Foto: bunte Ring-Wire-Bindungen" style="background:linear-gradient(180deg,#e9e9e9 0,#e9e9e9 18%,#f4d21b 30%,#e3332a 55%,#c7c7c7 80%,#9a9a9a)"></div><div class="lbl">Ring-Wire-Bindung</div></div>
  <div class="bcard active" style="left:359px"><div class="img" role="img" aria-label="Foto: Block mit Spiralbindung auf Holztisch" style="background:linear-gradient(135deg,#8b6a4b,#a98563 35%,#e8e8e6 36%,#f1f1ef 70%,#2fa8cf 71%)"></div><div class="lbl">Spiralbindung</div></div>
  <div class="bcard" style="left:613px"><div class="img" role="img" aria-label="Foto: Leinenfälzel in Blau und Grün" style="background:repeating-linear-gradient(115deg,#2d3f8f 0 34px,#4e9a3d 34px 68px)"></div><div class="lbl">Leinenfälzel</div></div>
  <div class="bcard" style="left:865px"><div class="img" role="img" aria-label="Foto: Klappfälzel auf orangem Grund" style="background:linear-gradient(125deg,#f26b3a 0,#f47c4a 55%,#8fc9e6 56%,#a6d7ee)"></div><div class="lbl">Klappfälzel</div></div>
  <a class="btn" href="#" style="left:533px;top:444px;width:136px;height:31px">Alle Ansehen</a>
</section>

<section class="service">
  <h2 class="section-title script" style="top:76px">Service aus einer hand - Kompetenz verbindet!</h2>
  <div class="scard" style="left:106px">
    <div class="img" role="img" aria-label="Foto: Tischkalender mit Ringbindung" style="background:linear-gradient(135deg,#d7d8da,#a7acb3 50%,#6e757d)"></div>
    <div class="icon"><svg width="40" height="40" viewBox="0 0 40 40"><path d="M8 12h24l-12 22z" fill="none" stroke="#1d1d1d" stroke-width="2"/><path d="M8 12l6-6h12l6 6M14 12l6 22M26 12l-6 22M14 6l6 6 6-6" fill="none" stroke="#ee0000" stroke-width="2"/></svg></div>
    <h3 class="script">Exklusives</h3>
    <p>Außergewöhnliche Herausforderungen sind unsere Spezialität - Exklusivität ist unser Markenzeichen.</p>
    <a class="btn btn-outline" href="#">Mehr Info</a>
  </div>
  <div class="scard" style="left:613px">
    <div class="img" role="img" aria-label="Foto: Kalender mit Spiralbindung" style="background:linear-gradient(135deg,#7f8f9a,#3a8fb8 45%,#e3332a 70%,#f0f0f0)"></div>
    <div class="icon"><svg width="36" height="36" viewBox="0 0 36 36"><rect x="9" y="6" width="18" height="24" fill="none" stroke="#1d1d1d" stroke-width="2"/><path d="M13 12h10M13 17h10M13 22h7" stroke="#ee0000" stroke-width="2"/></svg></div>
    <h3 class="script">Technische Informationen</h3>
    <p>Wenns mal ins Detail geht soll, stehen wir Ihnen mit Rat zur Seite. Damit Sie optimale Produkte vorzeigen können.</p>
    <a class="btn btn-outline" href="#">Mehr Info</a>
  </div>
</section>

<section class="team">
  <span class="eyebrow">Unser Team</span>
  <h2>Seit über 50 jahren beraten wir kunden im In- und Ausland - ideenreich bei allen fragen rund um design und funktion ihrer produkte.</h2>
  <div class="tcard" style="left:106px">
    <div class="photo" role="img" aria-label="Porträtfoto des Geschäftsführers"></div>
    <h3 class="script">Dipl.-Ing. (FH) Markus Feldner</h3>
    <span class="role">Geschäftsführer / CEO</span>
    <span class="row" style="top:149px"><svg width="11" height="11" viewBox="0 0 24 24"><path fill="#ee0000" d="M6.6 10.8a15 15 0 006.6 6.6l2.2-2.2c.3-.3.7-.4 1-.2 1.1.4 2.3.6 3.6.6.6 0 1 .4 1 1V20c0 .6-.4 1-1 1A17 17 0 013 4c0-.6.4-1 1-1h3.5c.6 0 1 .4 1 1 0 1.3.2 2.5.6 3.6.1.3 0 .7-.2 1z"/></svg>(+49) 0 84 21/55 30-0</span>
    <span class="row" style="top:176px"><svg width="11" height="11" viewBox="0 0 24 24"><circle cx="12" cy="12" r="10" fill="#ee0000"/><path d="M7 9h10v7H7z M7 9l5 4 5-4" fill="none" stroke="#fff" stroke-width="1.5"/></svg>feldner@brenkow-gmbh.example</span>
    <a class="more" href="#">Mehr Info</a>
  </div>
  <div class="tcard" style="left:613px">
    <div class="photo" role="img" aria-label="Porträtfoto des Prokuristen"></div>
    <h3 class="script">Dipl.-Ing. (FH) Stefan Wolmer</h3>
    <span class="role">Prokurist - Vertriebsleitung</span>
    <span class="row" style="top:149px"><svg width="11" height="11" viewBox="0 0 24 24"><path fill="#ee0000" d="M6.6 10.8a15 15 0 006.6 6.6l2.2-2.2c.3-.3.7-.4 1-.2 1.1.4 2.3.6 3.6.6.6 0 1 .4 1 1V20c0 .6-.4 1-1 1A17 17 0 013 4c0-.6.4-1 1-1h3.5c.6 0 1 .4 1 1 0 1.3.2 2.5.6 3.6.1.3 0 .7-.2 1z"/></svg>(+49) 0 84 21/55 30-19</span>
    <span class="row" style="top:176px"><svg width="11" height="11" viewBox="0 0 24 24"><circle cx="12" cy="12" r="10" fill="#ee0000"/><path d="M7 9h10v7H7z M7 9l5 4 5-4" fill="none" stroke="#fff" stroke-width="1.5"/></svg>s.wolmer@brenkow-gmbh.example</span>
    <a class="more" href="#">Mehr Info</a>
  </div>
  <span class="arrow" style="left:91px;top:447px"><svg width="10" height="10" viewBox="0 0 10 10"><path d="M6.5 1.5L3 5l3.5 3.5" fill="none" stroke="#ee0000" stroke-width="1.6"/></svg></span>
  <span class="arrow" style="left:1078px;top:447px"><svg width="10" height="10" viewBox="0 0 10 10"><path d="M3.5 1.5L7 5 3.5 8.5" fill="none" stroke="#ee0000" stroke-width="1.6"/></svg></span>
  <a class="btn" href="#" style="left:533px;top:648px;width:136px;height:31px">Alle Ansehen</a>
</section>

<section class="why">
  <span class="eyebrow" style="left:199px;top:52px">Warum wählen Sie ...</span>
  <h2 class="script">Die ganze welt der anleihen!</h2>
  <span class="tag">Ihr kompetenter Partner für</span>
  <span class="check" style="left:199px;top:228px"><svg width="20" height="12" viewBox="0 0 20 12"><path d="M1 6l4 4 7-9M8 10l8-9" fill="none" stroke="#ee0000" stroke-width="1.6"/></svg>Über 50 Jahre Erfahrung</span>
  <span class="check" style="left:405px;top:228px"><svg width="20" height="12" viewBox="0 0 20 12"><path d="M1 6l4 4 7-9M8 10l8-9" fill="none" stroke="#ee0000" stroke-width="1.6"/></svg>Technisches Know-how</span>
  <span class="check" style="left:199px;top:267px"><svg width="20" height="12" viewBox="0 0 20 12"><path d="M1 6l4 4 7-9M8 10l8-9" fill="none" stroke="#ee0000" stroke-width="1.6"/></svg>Individuelle Beratung</span>
  <span class="check" style="left:405px;top:267px"><svg width="20" height="12" viewBox="0 0 20 12"><path d="M1 6l4 4 7-9M8 10l8-9" fill="none" stroke="#ee0000" stroke-width="1.6"/></svg>Langjährige Geschäftsverbindungen</span>
  <span class="check" style="left:199px;top:305px"><svg width="20" height="12" viewBox="0 0 20 12"><path d="M1 6l4 4 7-9M8 10l8-9" fill="none" stroke="#ee0000" stroke-width="1.6"/></svg>Ausgebildetes Fachpersonal</span>
  <a class="btn" href="#" style="left:199px;top:355px;width:201px;height:30px">Jetzt Angebot anfordern</a>
  <div class="ring"></div>
  <div class="circle" role="img" aria-label="Foto: Tischkalender Februar mit Gemüse-Illustration"></div>
</section>

<section class="gallery">
  <span class="eyebrow" style="left:0;width:1200px;text-align:center;top:74px">Fotogalerie</span>
  <h2 class="section-title script" style="top:100px">Übersicht diverser Referenzen</h2>
  <div class="filters">
    <span class="on" style="left:0;width:55px">Alle</span>
    <span style="left:63px;width:77px">Kalender</span>
    <span style="left:150px;width:150px">Bücher u. lose Blattwerke</span>
    <span style="left:308px;width:87px">Exklusives</span>
    <span style="left:403px;width:89px">Produktion</span>
  </div>
  <div class="gimg" role="img" aria-label="Foto: Tischkalender mit Tiermotiv" style="left:106px;top:273px;width:251px;height:250px;background:linear-gradient(160deg,#c9d6a0,#e9b67a 50%,#6f8fc4 85%)"></div>
  <div class="gimg" role="img" aria-label="Foto: Wandkalender mit Berglandschaft und Spiralbindung" style="left:383px;top:234px;width:436px;height:332px;background:linear-gradient(180deg,#d9dadb 0,#d9dadb 18%,#8fb4cc 30%,#2f5a6e 55%,#6b8f9f 75%,#d9dadb 90%)"></div>
  <div class="gimg" role="img" aria-label="Foto: Schmaler Wandkalender 2020 mit Steinbock" style="left:844px;top:273px;width:250px;height:250px;background:linear-gradient(150deg,#e6e6e6,#a9b7c6 45%,#6f6658 80%)"></div>
  <span class="arrow" style="left:91px;top:384px"><svg width="10" height="10" viewBox="0 0 10 10"><path d="M6.5 1.5L3 5l3.5 3.5" fill="none" stroke="#ee0000" stroke-width="1.6"/></svg></span>
  <span class="arrow" style="left:1079px;top:384px"><svg width="10" height="10" viewBox="0 0 10 10"><path d="M3.5 1.5L7 5 3.5 8.5" fill="none" stroke="#ee0000" stroke-width="1.6"/></svg></span>
</section>

<footer class="footer">
  <a class="logo" href="#">Brenkow</a>
  <p class="about-txt">Der Druckweiterverarbeiter Brenkow ist eine der größten Kalenderfabriken Deutschlands mit vier vollautomatischen Kalenderstraßen.</p>
  <span class="social" style="left:199px"></span>
  <span class="social" style="left:231px"></span>
  <span class="social" style="left:263px"></span>

  <h4 style="left:505px">Kontakt zu uns</h4>
  <span class="frow" style="top:133px;font-size:12px;color:#fff"><svg width="11" height="11" viewBox="0 0 24 24"><path fill="#ee0000" d="M6.6 10.8a15 15 0 006.6 6.6l2.2-2.2c.3-.3.7-.4 1-.2 1.1.4 2.3.6 3.6.6.6 0 1 .4 1 1V20c0 .6-.4 1-1 1A17 17 0 013 4c0-.6.4-1 1-1h3.5c.6 0 1 .4 1 1 0 1.3.2 2.5.6 3.6.1.3 0 .7-.2 1z"/></svg>+49 (8421) 5530-0</span>
  <span class="frow" style="top:159px"><svg width="11" height="9" viewBox="0 0 24 18"><rect width="24" height="18" fill="#ee0000"/><path d="M2 2l10 7 10-7" fill="none" stroke="#262626" stroke-width="2"/></svg>info@brenkow-gmbh.example</span>
  <span class="frow" style="top:184px"><svg width="11" height="12" viewBox="0 0 24 28"><path fill="#ee0000" d="M12 0a10 10 0 0110 10c0 7-10 18-10 18S2 17 2 10A10 10 0 0112 0z"/><circle cx="12" cy="10" r="4" fill="#262626"/></svg>Brenkow GmbH &amp; Co. KG Lindenhofweg 14</span>
  <span class="frow" style="top:208px;left:524px">84112 Talbrunn</span>
  <span class="frow" style="top:236px;left:524px;color:var(--red)">Zur Anfahrt →</span>

  <h4 style="left:819px">Schnelle Links</h4>
  <div class="links">
    <a style="left:819px;top:133px">Home</a><a style="left:919px;top:133px">Kontakt</a>
    <a style="left:819px;top:155px">Unternehmen</a><a style="left:919px;top:155px">Impressum</a>
    <a style="left:819px;top:177px">Bindungen</a><a style="left:919px;top:177px">Cookies</a>
    <a style="left:819px;top:200px">Exklusives</a><a style="left:919px;top:200px">Datenschutz</a>
    <a style="left:819px;top:222px">Galerie</a>
    <a style="left:819px;top:244px">Service</a>
  </div>
  <svg class="abs" style="left:1087px;top:281px" width="14" height="12" viewBox="0 0 14 12"><path d="M7 0l7 12H0z" fill="#ee0000"/></svg>
  <div class="rule"></div>
  <p class="copy">© 2025 <b>Brenkow GmbH &amp; Co. KG</b> - Ringwirebindungen - Drahtkammbindungen - Kalenderbindungen - Talbrunn</p>
</footer>

</body>
</html>
```